The Corvel Dental centre, the Zorvik of dentistry

New concept of running a dental practice by having a walk in practice
WE ARE A HUSBAND AND WIFE TEAM

Really modern and sophisticated, we want it to feel different from the traditional dental practice.
we want it split into different pages:CONTACT US
LOCATION: Information about our location since patients often confuse us with the practice across the road
ABOUT US:
Opening hours - & 7 Days, We offer a weekend service
WALK IN: We offer a walk in service for dental treatments
TREATMENTS we offer

DENTAL ADVICE: Free dentist advise call back- So a dentist will call you back for free to discuss

Target Market(s)

Everyone

Industry/Entity Type

Dental

Coding

Coded - Design and coding required

Number of Pages Required

5+ page

Requirements
Must have
• First page
• * changing pictures
• *opening times
• * our walk in concept I.e. no appointment needed
• *logo
• * links in to medi portal (online booking system in Australia)
• * address /phone number/email
• * possible videos
• Second page
• meet the team
• third page
• dental treatments/walk in treatments
• fourth page
• dental advice with you tube videos
• Fifth page
• contact us/maps/ we get confused with the dental practice across the road
• We would also like a giving back page. In this please include the photo's below of our dental mission in Guatemala, where by we did treatment for patients as part of a charity.
Nice to have
• Changing pictures on the home screen
• videos linked to home page

```html
<!DOCTYPE html>
<html lang="en">
<head>
<meta charset="utf-8">
<title>The Corvel Dental centre</title>
<link href="https://fonts.googleapis.com/css2?family=Roboto:wght@300;400;500;700&display=swap" rel="stylesheet">
<style>
:root{
  --green:#a6cf43;
  --blue:#02a9e8;
  --grey:#6d6d6d;
  --dark:#444;
  --line:#e4e4e4;
  --orange:#f58a07;
  --white:#fff;
}
*{margin:0;padding:0;box-sizing:border-box}
html,body{width:746px;height:1200px;overflow:hidden;background:var(--white)}
body{font-family:'Roboto',sans-serif;color:var(--dark);position:relative}
.site-header{position:absolute;top:0;left:0;width:746px;height:80px;border-bottom:1px solid var(--line)}
.brand{position:absolute;left:58px;top:30px;display:flex;align-items:center;gap:8px}
.brand-mark{width:14px;height:14px;border-radius:50%;background:var(--green)}
.brand-name{font-size:19px;font-weight:700;color:var(--green)}
.header-contact{position:absolute;right:52px;top:36px;text-align:right}
.header-contact .lead{font-size:11.5px;color:var(--grey);font-weight:300}
.header-contact .lead b{color:var(--blue);font-weight:500}
.header-contact .phone{font-size:17px;font-weight:300;color:var(--grey);letter-spacing:.3px}
.main-nav{position:absolute;top:80px;left:0;width:746px;height:27px;border-bottom:1px solid var(--line);font-size:8.5px;color:var(--dark)}
.main-nav ul{list-style:none;display:flex;align-items:center;height:26px;padding-left:55px}
.main-nav li{display:flex;align-items:center;height:100%}
.main-nav li+li::before{content:"|";color:var(--blue);margin:0 8px}
.main-nav li.active{background:var(--green);color:var(--white);font-weight:700;padding:0 12px;margin-right:6px}
.main-nav li.active+li::before{content:none}
.hero{position:absolute;top:119px;left:55px;width:636px;height:186px;border-radius:7px;overflow:hidden;display:flex}
.hero-text{width:284px;background:var(--blue);color:var(--white);padding:35px 0 0 42px}
.hero-text h1{font-size:33px;font-weight:700;line-height:1}
.hero-text .strong{font-size:18px;font-weight:500;line-height:1.08;margin-top:4px}
.hero-text .light{font-size:18px;font-weight:300;line-height:1.08}
.hero-photo{flex:1;background:radial-gradient(ellipse at 72% 45%,#f3cfae 0%,#e9c39e 18%,rgba(233,195,158,0) 42%),radial-gradient(ellipse at 78% 20%,#f1dc9a 0%,rgba(241,220,154,0) 35%),linear-gradient(100deg,#cfd9e0 0%,#eef1f3 35%,#e6ecef 60%,#7fa7a8 100%)}
.cards{position:absolute;top:325px;left:54px;width:638px;display:flex;justify-content:space-between}
.card{width:202px;height:215px;border-radius:7px;overflow:hidden;color:var(--white);position:relative}
.card.green{background:var(--green)}
.card.blue{background:var(--blue)}
.card-title{height:71px;padding:22px 0 0 21px;font-size:17px;font-weight:300;line-height:1.1}
.card-photo{height:61px}
.card.green .card-photo{background:linear-gradient(165deg,#f4f7f9 0%,#e3ecf2 45%,#b9cfdc 70%,#2aa7a0 74%,#eef3f6 80%)}
.card.blue .card-photo{background:linear-gradient(90deg,#2a7fb4 0%,#4aa3d6 18%,#f1cdb5 40%,#f6e3d6 58%,#b9c7cf 78%,#7c8f99 100%)}
.card-body{text-align:center;font-size:7px;font-weight:500;line-height:1.3;padding:14px 8px 0}
.card-body .link{margin-top:22px}
.card.blue .card-body .link{margin-top:12px}
.card.team{background:radial-gradient(ellipse at 30% 45%,#c79a7c 0%,rgba(199,154,124,0) 30%),radial-gradient(ellipse at 75% 30%,#9b6d50 0%,rgba(155,109,80,0) 28%),linear-gradient(180deg,#f1f2f3 0%,#dfe3e6 30%,#6a9ac8 60%,#2f5a4b 100%);border:1px solid var(--line)}
.team-caption{position:absolute;bottom:0;left:0;right:0;height:63px;background:rgba(30,40,60,.78);text-align:center;padding-top:10px}
.team-caption h3{font-size:13px;font-weight:500;color:var(--green)}
.team-caption p{font-size:7.5px;line-height:1.3;margin-top:3px}
.quote{position:absolute;top:568px;left:0;width:746px;text-align:center}
.quote p{font-size:13px;font-weight:300;color:var(--grey)}
.quote cite{display:block;font-style:normal;font-size:11.5px;font-weight:500;color:var(--grey);margin-top:3px}
.qmark{position:absolute;top:-8px;font-size:34px;font-weight:700;color:var(--blue);font-family:Georgia,serif}
.qmark.open{left:130px}.qmark.close{left:578px}
.testimonials{position:absolute;top:632px;left:0;width:746px;height:198px;background:var(--green);color:var(--white)}
.section-title{position:absolute;top:28px;left:54px;width:638px;display:flex;align-items:center;gap:14px;font-size:19px;font-weight:400}
.section-title::before,.section-title::after{content:"";flex:1;height:1px;background:rgba(255,255,255,.8)}
.testimonial{position:absolute;top:77px;width:300px;padding-left:84px}
.testimonial .avatar{position:absolute;left:0;top:0;width:68px;height:68px;border-radius:50%;border:2px solid var(--white)}
.t1 .avatar{background:radial-gradient(circle at 50% 42%,#e2b793 0%,#c99474 32%,#8b8e94 60%,#3c4047 100%)}
.t2 .avatar{background:radial-gradient(circle at 50% 45%,#f0c7ad 0%,#d9a487 35%,#6b4332 62%,#f3f1ee 100%)}
.testimonial .date{font-size:7px;font-weight:700}
.testimonial .text{font-size:8.4px;line-height:1.28;margin-top:7px;width:215px}
.testimonial .more{display:inline-block;font-size:9px;font-weight:700;color:var(--orange);margin-top:5px}
.t1{left:57px}.t2{left:390px}
.mission{position:absolute;top:830px;left:0;width:746px;height:198px;background:var(--blue)}
.mission h2{text-align:center;color:var(--white);font-size:17px;font-weight:500;margin-top:26px}
.mission-photo{position:absolute;top:886px;left:59px;width:629px;height:264px;border:2px solid var(--green);border-radius:9px;background:linear-gradient(90deg,rgba(0,0,0,0) 75%,rgba(110,90,75,.55) 100%),linear-gradient(180deg,#ece8e3 0%,#d8d1c8 18%,#7f9ac6 40%,#4d6aa0 62%,#3a4a6e 82%,#c9574d 92%,#d8d3cd 100%)}
.site-footer{position:absolute;top:1166px;left:54px;width:638px;border-top:1px solid var(--line);text-align:center;font-size:8px;color:var(--grey);padding-top:8px}
.site-footer span+span::before{content:"|";margin:0 8px}
</style>
</head>
<body>
<header class="site-header">
  <div class="brand"><span class="brand-mark"></span><span class="brand-name">The Corvel Dental centre</span></div>
  <div class="header-contact">
    <div class="lead"><b>Walk in appointments available,</b> call today to find out more</div>
    <div class="phone">0140-555-2871</div>
  </div>
</header>
<nav class="main-nav">
  <ul>
    <li class="active">Home</li>
    <li>Meet the Team</li>
    <li>Dental treatments/Walk in treatments</li>
    <li>Dental advice</li>
    <li>Contact Us</li>
  </ul>
</nav>
<section class="hero">
  <div class="hero-text">
    <h1>Nervous,</h1>
    <div class="strong">don’t worry we can help<br>relieve your fears,</div>
    <div class="light">come in and have a chat with<br>our friendly dentists.</div>
  </div>
  <div class="hero-photo" role="img" aria-label="Smiling young patient in a dental chair with a dentist"></div>
</section>
<section class="cards">
  <article class="card green">
    <div class="card-title">Weekend &amp; Emergency<br>Appointments</div>
    <div class="card-photo" role="img" aria-label="Dentist's hands folded over a desk with documents"></div>
    <div class="card-body">Weekend &amp; Emergency Appointments<div class="link">click for office hours</div></div>
  </article>
  <article class="card blue">
    <div class="card-title">New Patient<br>Specials ★</div>
    <div class="card-photo" role="img" aria-label="Smiling patient being examined by a dentist"></div>
    <div class="card-body">Free exam and consultation for non-insured patients!<br>Free teeth whitening for insured patients!<br>(PPO only)<div class="link">click to print coupons</div></div>
  </article>
  <article class="card team" role="img" aria-label="Portrait of the two dentists who run the practice">
    <div class="team-caption">
      <h3>Mara and Dilan</h3>
      <p>We want our patients to feel safe, happy and<br>have dental treatment which is accessible.</p>
    </div>
  </article>
</section>
<blockquote class="quote">
  <span class="qmark open">“</span><span class="qmark close">”</span>
  <p>A dentist at work in his vocation always looks down in the mouth.</p>
  <cite>Harold T. Winslow</cite>
</blockquote>
<section class="testimonials">
  <h2 class="section-title">TESTIMONIALS</h2>
  <div class="testimonial t1">
    <div class="avatar" role="img" aria-label="Photo of a male patient"></div>
    <div class="date">7 December 2014</div>
    <div class="text">Dummy text to be replaced here, dummy text to be replaced here, dummy text to be replaced here.here, dummy text to be replaced here, dummy text to be replaced here.here, dummy text to be replaced here, dummy text to be replaced here.here,</div>
    <a class="more">+ read more</a>
  </div>
  <div class="testimonial t2">
    <div class="avatar" role="img" aria-label="Photo of a female patient"></div>
    <div class="date">8 June 2014</div>
    <div class="text">Dummy text to be replaced here, dummy text to be replaced here, dummy text to be replaced here.here, dummy text to be replaced here, dummy text to be replaced here.here, dummy text to be replaced here, dummy text to be replaced here.here,</div>
    <a class="more">+ read more</a>
  </div>
</section>
<section class="mission"><h2>Dental Mission</h2></section>
<div class="mission-photo" role="img" aria-label="Group photo of the dental mission volunteer team in Guatemala"></div>
<footer class="site-footer">
  <span>Home</span><span>Meet the Team</span><span>Dental treatments/Walk in treatments</span><span>Dental advice</span><span>Contact Us</span>
</footer>
</body>
</html>
```